Speisekarten-Design für Tennis- und Freizeitanlage mit Restaurant und Biergarten
Zielgruppe
Tennis- und Freizeitanlage mit Restaurant und Biergarten. Zielgruppe von Jung bis Alt
Aufgabenstellung
Speise- und Getränkekarte. Klassisch und klar strukturiert. Möglichst zum selbst ausdrucken (kein Randloses Design) Möglichkeit zum selbstständigen ändern als Word Dokument. A4 Format. Hülle der Speisekarte bereits vorhanden. Siehe Fotos
Wenn möglich farbiges Logo verwenden. Alternativ habe ich noch eine schwarz weiß Variante hinzugefügt.

```html
<!DOCTYPE html>
<html lang="de">
<head>
<meta charset="utf-8">
<title>Speisekarte – Restaurant &amp; Biergarten</title>
<link rel="stylesheet" href="https://fonts.googleapis.com/css2?family=Marcellus+SC&family=Marcellus&family=Inter:wght@400&display=swap">
<style>
  :root {
    --backdrop: #48654f;
    --paper: #ebe8e3;
    --forest: #3f6450;
    --ink: #4a4f4c;
    --scene-sky: #a9c4d8;
    --scene-trees: #4f7a45;
    --scene-lawn: #6e9a55;
    --scene-table: #d9d2c6;
  }
  * { box-sizing: border-box; margin: 0; padding: 0; }
  html, body { width: 1200px; height: 900px; overflow: hidden; }
  body { background: var(--backdrop); position: relative; }

  .menu-card {
    position: absolute;
    left: 344px; top: 76px;
    width: 512px; height: 747px;
    background: var(--paper);
  }
  .frame-lines {
    position: absolute; inset: 0;
    width: 512px; height: 747px;
  }
  .frame-lines path { fill: none; stroke: var(--forest); stroke-width: 1.4; }

  .crest {
    position: absolute;
    left: 226px; top: 72px;
    width: 60px; height: 56px;
    border-radius: 6px;
    background: linear-gradient(135deg, #c9d3cc, #b3c2b8);
  }
  .menu-title {
    position: absolute;
    top: 142px; left: 0; right: 0;
    text-align: center;
    font-family: "Marcellus SC", serif;
    font-size: 72px;
    line-height: 1;
    color: var(--forest);
    letter-spacing: 1px;
  }
  .venue-type {
    position: absolute;
    left: 0; right: 0;
    text-align: center;
    font-family: "Marcellus", serif;
    color: var(--forest);
    text-transform: uppercase;
    line-height: 1;
  }
  .venue-type.restaurant { top: 219px; font-size: 19px; letter-spacing: 0.5px; }
  .venue-type.garden { top: 240px; font-size: 15px; letter-spacing: 0.5px; }

  .garden-scene {
    position: absolute;
    left: 0; top: 291px;
    width: 512px; height: 298px;
    background: linear-gradient(180deg,
      var(--scene-sky) 0%,
      var(--scene-trees) 25%,
      #3f5f48 45%,
      var(--scene-lawn) 62%,
      var(--scene-table) 80%,
      #b9b1a4 100%);
  }

  .info-table {
    position: absolute;
    top: 618px; left: 0; right: 0;
    font-family: "Inter", sans-serif;
    font-size: 11.5px;
    color: var(--ink);
  }
  .info-row { position: absolute; white-space: nowrap; }
  .info-label.left { left: 71px; }
  .info-value.left { left: 205px; }
  .info-label.right { left: 281px; }
  .info-value.right { left: 414px; }
  .info-divider {
    position: absolute;
    left: 256px; top: 618px;
    width: 1px; height: 50px;
    background: var(--ink);
  }
</style>
</head>
<body>
  <main class="menu-card">
    <svg class="frame-lines" viewBox="0 0 512 747" aria-hidden="true">
      <path d="M26,291 V39 A14 14 0 0 0 40 25 H472 A14 14 0 0 0 486 39 V291"/>
      <path d="M31,291 V43.3 A19 19 0 0 0 44.3 30 H467.7 A19 19 0 0 0 481 43.3 V291"/>
      <path d="M26,591 V710 A14 14 0 0 1 40 724 H472 A14 14 0 0 1 486 710 V591"/>
      <path d="M31,591 V705.7 A19 19 0 0 1 44.3 719 H467.7 A19 19 0 0 1 481 705.7 V591"/>
    </svg>

    <div class="crest" role="img" aria-label="Emblem mit zwei gekreuzten Tennisschlägern"></div>
    <h1 class="menu-title">Menu</h1>
    <p class="venue-type restaurant">Restaurant</p>
    <p class="venue-type garden">Beer Garden</p>

    <div class="garden-scene" role="img" aria-label="Illustration: Gäste mit Bier und Speisen an Tischen unter Sonnenschirmen im Biergarten neben dem Tennisplatz"></div>

    <div class="info-table">
      <span class="info-row info-label left" style="top:0">Contact Phone</span>
      <span class="info-row info-value left" style="top:0">180</span>
      <span class="info-row info-label left" style="top:18px">Opening Times</span>
      <span class="info-row info-value left" style="top:18px">554</span>
      <span class="info-row info-label left" style="top:36px">Order Online</span>
      <span class="info-row info-value left" style="top:36px">91</span>

      <span class="info-row info-label right" style="top:0">Opening Hours</span>
      <span class="info-row info-value right" style="top:0">910</span>
      <span class="info-row info-label right" style="top:18px">Openings</span>
      <span class="info-row info-value right" style="top:18px">918</span>
      <span class="info-row info-label right" style="top:36px">Address Details</span>
      <span class="info-row info-value right" style="top:36px">570</span>
    </div>
    <div class="info-divider"></div>
  </main>
</body>
</html>
```